Business Card Design

Harlow Sun and Electrical is a new company that specializes in solar pv. I need a card with similar attributes to the ones I have attached. I am after a two sided card with the logo on one side and the logo plus info on the other. I would prefer one side to be black and the other to be a colour but am open to suggestions. The colour scheme I was thinking of was blue or green. I plan on spot glossing the logos if that makes any difference. I have attached a file of my logo in a few colours, none of which I am completely sold on so please feel free to change colous to suit.
Thanks.
Contact Information for Business Card
Dorian Harlow, www.hwx-example.net.nz, dorian@hwx-example.net.nz, t. 0508 4 BRIGHT m. 027469318

```html
<!DOCTYPE html>
<html lang="en">
<head>
<meta charset="utf-8">
<title>Harlow Sun and Electrical — Business Card</title>
<link rel="stylesheet" href="https://fonts.googleapis.com/css2?family=Questrial&display=swap">
<style>
  :root {
    --backdrop: #aeadb2;
    --green-bright: #35d53a;
    --green-soft: #30c15e;
    --green-deep: #22b06a;
    --charcoal: #2d2d2d;
    --logo-blue: #1d5fe6;
    --ink-light: #f2f2f2;
    --shadow: rgba(0, 0, 0, 0.45);
  }
  * { margin: 0; padding: 0; box-sizing: border-box; }
  html, body {
    width: 1125px;
    height: 1200px;
    overflow: hidden;
    background: var(--backdrop);
    font-family: "Questrial", sans-serif;
  }
  .canvas { position: relative; width: 1125px; height: 1200px; }

  .card {
    position: absolute;
    left: 100px;
    width: 921px;
    height: 569px;
    box-shadow: 3px 4px 6px var(--shadow);
    overflow: hidden;
  }

  /* Front */
  .card-front {
    top: 27px;
    background: radial-gradient(ellipse at 50% 0%, var(--green-bright) 0%, var(--green-soft) 75%, #2fbf62 100%);
  }
  .front-wordmark {
    position: absolute;
    left: 0; right: 0;
    top: 262px;
    text-align: center;
    font-size: 56px;
    color: var(--logo-blue);
    letter-spacing: 1px;
    white-space: nowrap;
  }

  /* Back */
  .card-back { top: 611px; background: var(--charcoal); }
  .contact-name {
    position: absolute;
    left: 484px;
    top: 62px;
    font-size: 25px;
    color: var(--ink-light);
    letter-spacing: 0.3px;
  }
  .contact-list { position: absolute; left: 512px; top: 142px; list-style: none; }
  .contact-item {
    position: absolute;
    left: 0;
    display: flex;
    align-items: center;
    gap: 11px;
    font-size: 16px;
    color: var(--ink-light);
    white-space: nowrap;
  }
  .contact-item svg { width: 16px; height: 16px; flex: none; }
  .contact-item.web { top: 0; }
  .contact-item.mail { top: 41px; }
  .contact-item.phone { top: 102px; }
  .contact-item.mobile { top: 145px; }

  .brand-band {
    position: absolute;
    left: 0;
    top: 341px;
    width: 921px;
    height: 163px;
    background: linear-gradient(90deg, var(--green-soft), #33c75a);
  }
  .brand-band svg.band-corner { position: absolute; left: 0; top: 0; }
  .band-wordmark {
    position: absolute;
    left: 24px;
    top: 58px;
    font-size: 33px;
    color: var(--logo-blue);
    white-space: nowrap;
  }
</style>
</head>
<body>
<main class="canvas">
  <section class="card card-front" aria-label="Card front">
    <div class="front-wordmark">Harlow Sun and Electrical</div>
  </section>

  <section class="card card-back" aria-label="Card back">
    <h1 class="contact-name" style="font-weight:400">Dorian Harlow</h1>
    <ul class="contact-list">
      <li class="contact-item web">
        <svg viewBox="0 0 16 16" fill="none" stroke="#e6e6e6" stroke-width="1"><circle cx="8" cy="8" r="6.5"/><ellipse cx="8" cy="8" rx="3" ry="6.5"/><line x1="1.5" y1="8" x2="14.5" y2="8"/><line x1="2.5" y1="4.5" x2="13.5" y2="4.5"/><line x1="2.5" y1="11.5" x2="13.5" y2="11.5"/></svg>
        <span>www.hwx-example.net.nz</span>
      </li>
      <li class="contact-item mail">
        <svg viewBox="0 0 16 16" fill="none" stroke="#e6e6e6" stroke-width="1"><rect x="1.5" y="3.5" width="13" height="9"/><polyline points="1.5,3.5 8,9 14.5,3.5"/></svg>
        <span>dorian@hwx-example.net.nz</span>
      </li>
      <li class="contact-item phone">
        <svg viewBox="0 0 16 16" fill="none" stroke="#e6e6e6" stroke-width="1"><path d="M1.5 6 Q8 1 14.5 6 L13 8 L10.5 7 L10.5 5.5 Q8 4.8 5.5 5.5 L5.5 7 L3 8 Z"/><rect x="3.5" y="9" width="9" height="4.5" rx="1"/></svg>
        <span>t. 0508 4 BRIGHT</span>
      </li>
      <li class="contact-item mobile">
        <svg viewBox="0 0 16 16"><rect x="1" y="1" width="14" height="14" rx="2.5" fill="#f2f2f2"/><path d="M6 4 L7.5 6.5 L6.6 7.4 Q7.5 9.3 9 10 L9.9 9.1 L12 10.6 L11 12 Q7 12 4.8 6 Z" fill="#2d2d2d"/></svg>
        <span>m. 027469318</span>
      </li>
    </ul>

    <div class="brand-band">
      <svg class="band-corner" width="921" height="163" viewBox="0 0 921 163" aria-hidden="true">
        <polygon points="921,0 921,163 758,163" fill="var(--green-deep)" opacity="0.8"/>
      </svg>
      <div class="band-wordmark">Harlow Sun and Electrical</div>
    </div>
  </section>
</main>
</body>
</html>
```